Business Card Design

I am specialising in Designs, Drafting and Council approvals. From the idea to the full set of plans and other documents. Residential houses only.
I am located in Northern Beaches, Sydney where the sky is always blue :)
Tallwood Drafting should be associated with light, modern house designs & with 3D drafting. I am positive person, that would like help every client through the demanding time of council paperwork.

The business card should be light blue, with white 3D sketch and white or black writing. Simple, modern and "happy"

Please don't hesitate to suggest something if you think so.

Thanks
Mirela

Industry/Entity Type

House

Contact Information for Business Card

FRONT:

Tallwood Drafting
Servicing Northern Beaches

Mirela Ostrowe
tallwooddrafting@mailhaven.com.au
0427 586 293
www.tallwooddrafting.com.au

BACK:

Design consultation
Plans Drafting
3D Visualisation
Council Approvals

```html
<!DOCTYPE html>
<html lang="en">
<head>
<meta charset="utf-8">
<title>Tallwood Drafting — Business Card</title>
<link rel="stylesheet" href="https://fonts.googleapis.com/css2?family=Open+Sans:wght@400;600;700&display=swap">
<style>
  :root {
    --page-bg: #ecebe8;
    --sky-blue: #19b6ea;
    --sky-blue-deep: #0a9fd8;
    --ink: #1b2a33;
    --card-black: #1c1d1f;
    --card-black-soft: #2a2b2e;
    --accent-blue: #1fb3ea;
    --paper: #f4f4f4;
    --sketch-grey: #c9cbce;
    --white: #ffffff;
  }
  * { box-sizing: border-box; margin: 0; padding: 0; }
  html, body {
    width: 1200px; height: 800px; overflow: hidden;
    background: var(--page-bg);
    font-family: "Open Sans", Arial, sans-serif;
  }
  .stage {
    position: relative; width: 1200px; height: 800px;
    display: flex; align-items: center; justify-content: center; gap: 40px;
  }
  .card {
    position: relative; width: 550px; height: 314px; overflow: hidden;
    box-shadow: 0 10px 28px rgba(0,0,0,.18);
  }

  /* Back card */
  .card--back {
    background: linear-gradient(160deg, var(--sky-blue) 0%, var(--sky-blue-deep) 100%);
    color: var(--ink);
  }
  .back__area {
    position: absolute; top: 22px; right: 28px;
    font-size: 13px; letter-spacing: .06em; text-transform: uppercase;
  }
  .back__name {
    position: absolute; left: 0; right: 0; top: 112px;
    text-align: center; font-size: 40px; font-weight: 400; letter-spacing: .04em;
  }
  .back__services {
    position: absolute; left: 0; right: 0; bottom: 20px;
    text-align: center; font-size: 13px; word-spacing: .15em;
  }

  /* Front card */
  .card--front {
    background: linear-gradient(135deg, var(--card-black-soft) 0%, var(--card-black) 60%);
    color: var(--white);
  }
  .front__band { position: absolute; inset: 0; }
  .front__name {
    position: absolute; right: 24px; top: 22px; width: 210px;
    text-align: right; font-size: 30px; line-height: 1.1; font-weight: 400;
    color: var(--accent-blue); letter-spacing: .04em;
  }
  .front__person { position: absolute; left: 26px; top: 190px; }
  .front__person-name {
    font-size: 15px; font-weight: 700; color: var(--accent-blue);
    text-transform: uppercase; letter-spacing: .02em;
  }
  .front__person-role { font-size: 11px; padding-left: 22px; margin-top: 1px; }
  .front__contacts {
    position: absolute; left: 26px; bottom: 18px; list-style: none;
    font-size: 13px; line-height: 1.55;
  }
  .contact { display: flex; align-items: center; gap: 8px; }
  .contact__icon { width: 13px; height: 13px; flex: none; }
</style>
</head>
<body>
<main class="stage">

  <section class="card card--back" aria-label="Business card back">
    <p class="back__area">Northern Beaches</p>
    <h2 class="back__name">Tallwood Drafting</h2>
    <p class="back__services">Design consultation Plans Drafting 3D Visualisation Council Approvals</p>
  </section>

  <section class="card card--front" aria-label="Business card front">
    <svg class="front__band" viewBox="0 0 550 314" width="550" height="314" aria-hidden="false">
      <defs>
        <linearGradient id="sketch-tone" x1="0" y1="0" x2="1" y2="1">
          <stop offset="0" stop-color="#fbfbfb"/>
          <stop offset=".6" stop-color="#eeeff0"/>
          <stop offset="1" stop-color="#d6d8db"/>
        </linearGradient>
      </defs>
      <polygon points="0,20 550,150 550,270 0,120" fill="url(#sketch-tone)"
               role="img" aria-label="Floor plan drawing and 3D house sketch"/>
      <line x1="0" y1="16" x2="550" y2="146" stroke="var(--accent-blue)" stroke-width="3"/>
      <line x1="0" y1="124" x2="550" y2="274" stroke="var(--accent-blue)" stroke-width="3"/>
    </svg>

    <h1 class="front__name">Tallwood Drafting</h1>

    <div class="front__person">
      <p class="front__person-name">Mirela Ostrowe</p>
      <p class="front__person-role">Director</p>
    </div>

    <ul class="front__contacts">
      <li class="contact">
        <svg class="contact__icon" viewBox="0 0 13 13"><rect width="13" height="13" rx="2" fill="var(--accent-blue)"/><path d="M4 3h2l.6 2-1 .8a5 5 0 0 0 1.6 1.6l.8-1 2 .6v2c-3.5.3-6.3-2.5-6-6z" fill="var(--card-black)"/></svg>
        <span>0427 586 293</span>
      </li>
      <li class="contact">
        <svg class="contact__icon" viewBox="0 0 13 13"><rect width="13" height="13" rx="2" fill="var(--accent-blue)"/><rect x="3" y="4" width="7" height="5" fill="none" stroke="var(--card-black)" stroke-width="1"/><path d="M3 4l3.5 3L10 4" fill="none" stroke="var(--card-black)" stroke-width="1"/></svg>
        <span>tallwooddrafting@mailhaven.com.au</span>
      </li>
      <li class="contact">
        <svg class="contact__icon" viewBox="0 0 13 13"><rect width="13" height="13" rx="2" fill="var(--accent-blue)"/><circle cx="6.5" cy="6.5" r="3.5" fill="none" stroke="var(--card-black)" stroke-width="1"/><path d="M3 6.5h7M6.5 3v7" stroke="var(--card-black)" stroke-width="1"/></svg>
        <span>www.tallwooddrafting.com.au</span>
      </li>
    </ul>
  </section>

</main>
</body>
</html>
```